New Business Card for Web Design/Internet Marketing Company

Looking for a great looking new business card. We are a 10 year old web design, internet marketing and website management company that works mostly with small businesses.

Our new card needs to better match the colors and style of our website, be bold, extremely usable and slightly edgy.

Target Market(s)

Small/Medium businesses that have websites

Industry/Entity Type

Internet

Requirements
Must have
• Front and back design, full color, rounded corners please

Must use the colors/style of our website (JPG provided)

INFO FOR CARDS (as readable as possible please)
Mark Pellow
President/CEO
mark@brightlanesites.com
Phone: 520-481-7093
Toll Free: 866-481-7093
Address: 4315 E. Kestrel Ave. Ste. 140, Tucson, AZ 85733

THINGS I WANT TO PROMOTE (if there is room):
1. Our Website - www.brightlanesites.com

2. Social Media
Twitter: @brightlanesites
Facebook: www.facebook.com/brightlanesites

3. Our Services
Web Design
Internet Marketing
Website Management

```html
<!DOCTYPE html>
<html lang="en">
<head>
<meta charset="UTF-8">
<title>Bright Lane Sites – Business Card</title>
<link rel="stylesheet" href="https://fonts.googleapis.com/css2?family=Signika:wght@300;400;600&display=swap">
<style>
  :root {
    --bg: #1d1d1f;
    --card: #f7f7f5;
    --blue: #0a6cb4;
    --orange: #e8691d;
    --ink: #555558;
    --faint-blue: #dbe8f2;
  }
  * { margin: 0; padding: 0; box-sizing: border-box; }
  html, body { width: 1200px; height: 1080px; overflow: hidden; background: var(--bg); }
  body { position: relative; font-family: "Signika", sans-serif; color: var(--ink); }

  .card {
    position: absolute;
    top: 156px;
    width: 492px;
    height: 766px;
    background: var(--card);
    overflow: hidden;
  }
  .card--front { left: 90px; border-radius: 96px 0 96px 0; }
  .card--back  { left: 619px; border-radius: 0 72px 0 96px; }

  /* service stripes */
  .service-bar {
    position: absolute;
    top: 0;
    width: 14px;
    background: var(--blue);
  }
  .service-bar--design     { left: 396px; height: 90px; }
  .service-bar--marketing  { left: 426px; height: 132px; }
  .service-bar--management { left: 456px; height: 174px; }
  .service-label {
    position: absolute;
    writing-mode: vertical-rl;
    font-size: 19px;
    font-weight: 400;
    letter-spacing: 0.5px;
    color: var(--ink);
    line-height: 1;
  }
  .service-label--design     { left: 394px; top: 96px; }
  .service-label--marketing  { left: 424px; top: 138px; }
  .service-label--management { left: 454px; top: 180px; }

  /* front */
  .identity { position: absolute; right: 168px; top: 92px; text-align: right; }
  .identity__name { font-size: 54px; font-weight: 300; line-height: 1; letter-spacing: -0.5px; }
  .identity__first { color: var(--blue); }
  .identity__last { color: var(--orange); }
  .identity__title { font-size: 25px; font-weight: 400; margin-top: 4px; }

  .section-heading {
    position: absolute;
    left: 30px;
    font-size: 31px;
    font-weight: 600;
    color: var(--ink);
  }
  .section-heading__accent { color: var(--orange); }
  .section-heading--contact { top: 236px; }
  .section-heading--social  { top: 590px; }

  .contact-list { position: absolute; left: 30px; top: 286px; list-style: none; }
  .contact-list li { display: flex; font-size: 23px; height: 47px; align-items: center; }
  .contact-list__key { width: 42px; color: var(--blue); }

  .social-list { position: absolute; left: 30px; top: 640px; list-style: none; }
  .social-list li { display: flex; align-items: center; font-size: 23px; height: 47px; }
  .social-list__mark {
    width: 26px; height: 26px; border-radius: 4px; margin-right: 16px;
  }
  .social-list__mark--primary { background: #2aa3dc; }
  .social-list__mark--secondary { background: #2d5aa0; }

  .corner-band { position: absolute; left: 0; bottom: 0; width: 128px; height: 22px; background: var(--blue); }

  /* back */
  .back-decoration {
    position: absolute; left: -60px; top: 90px;
    width: 420px; height: 420px; border-radius: 50%;
    background: var(--faint-blue); opacity: 0.45;
  }
  .brand {
    position: absolute; left: 0; right: 0; top: 600px;
    display: flex; align-items: center; justify-content: center; gap: 14px;
  }
  .brand__dot { width: 30px; height: 30px; border-radius: 50%; background: var(--blue); }
  .brand__name { font-size: 40px; font-weight: 600; color: var(--orange); }
</style>
</head>
<body>

<section class="card card--front" aria-label="Business card front">
  <div class="service-bar service-bar--design"></div>
  <div class="service-bar service-bar--marketing"></div>
  <div class="service-bar service-bar--management"></div>
  <span class="service-label service-label--design">WEB DESIGN</span>
  <span class="service-label service-label--marketing">INTERNET MARKETING</span>
  <span class="service-label service-label--management">WEBSITE MANAGEMENT</span>

  <div class="identity">
    <h1 class="identity__name"><span class="identity__first">MARK</span> <span class="identity__last">PELLOW</span></h1>
    <p class="identity__title">President/CEO</p>
  </div>

  <h2 class="section-heading section-heading--contact"><span class="section-heading__accent">CONTACT</span> US</h2>
  <ul class="contact-list">
    <li><span class="contact-list__key">P.</span>520-481-7093</li>
    <li><span class="contact-list__key">T.</span>866-481-7093</li>
    <li><span class="contact-list__key">E.</span>mark@brightlanesites.com</li>
    <li><span class="contact-list__key">W.</span>www.brightlanesites.com</li>
    <li><span class="contact-list__key">A.</span>4315 E. Kestrel Ave.</li>
    <li><span class="contact-list__key"></span>Ste. 140, Tucson, AZ 85733</li>
  </ul>

  <h2 class="section-heading section-heading--social"><span class="section-heading__accent">SOCIAL</span> MEDIA</h2>
  <ul class="social-list">
    <li><span class="social-list__mark social-list__mark--primary"></span>@brightlanesites</li>
    <li><span class="social-list__mark social-list__mark--secondary"></span>/brightlanesites</li>
  </ul>

  <div class="corner-band"></div>
</section>

<section class="card card--back" aria-label="Business card back">
  <div class="back-decoration"></div>
  <div class="service-bar service-bar--design"></div>
  <div class="service-bar service-bar--marketing"></div>
  <div class="service-bar service-bar--management"></div>
  <span class="service-label service-label--design">WEB DESIGN</span>
  <span class="service-label service-label--marketing">INTERNET MARKETING</span>
  <span class="service-label service-label--management">WEBSITE MANAGEMENT</span>

  <div class="brand">
    <span class="brand__dot"></span>
    <span class="brand__name">Bright Lane Sites</span>
  </div>
</section>

</body>
</html>
```